Landing page needed for existing website. High Converting SaaS Landing Page!

Landing page needed for existing website. www.slotnudger.com.au

*Must be designed with Bootstrap framework in mind (so it looks great across all devices).
* Target market is small business owners who take many appointments each day. They want to reduce no shows and remind their customers of appointments dates and times.
* Highlight we intregrate into Plover Diary, Wickham Planner, Or use our Build in Web Calendar
* Competitors (bookvane.com, timeknelltrack.org)
* Clean modern fresh.
* http://quarrylanecreative.com/portfolio_category/web-design/ for inspiration
* Must have link for existing customers to login
* Navigation for future pages.
* Footer section for links to other pages (maybe a contact form)
* The aim of the page is to get prospects to start a Free trial.
* We have 3 domains. slotnudger.com.au (australian customers) slotnudger.co.nz (new zealand customers). slotnudger.info (US customers) these should be linked somewhere. Maybe in the footer with little flags.
Open to ideas on how the page should look. I would prefer something reasonably long with strong imagery.

Target Market(s)

Busy self employer business owners who have many appointments each day. Health professionals, Coaches, Financial Advisers, Tax Lawyers etc etc

Industry/Entity Type

Saas

Number of Pages Required

2 page

Font styles to use
Sans Serif

Requirements
Must have
• 1- Strong Landing Page.
• 2- Stripped down 2nd page that can be used for content, blog posts, content etc.
Nice to have
• Pricing Table

```html
<!DOCTYPE html>
<html lang="en">
<head>
<meta charset="utf-8">
<title>Text Appointment Reminders | Slot Nudger Blog</title>
<link href="https://fonts.googleapis.com/css2?family=Roboto:ital,wght@0,300;0,400;0,500;1,400&display=swap" rel="stylesheet">
<style>
:root{
  --green:#6cc36a;
  --green-icon:#5fb85c;
  --blue:#4a86f0;
  --ink:#2b2b2b;
  --text:#666;
  --nav:#555;
  --rule:#d9d9d9;
  --banner:#fbbd7f;
  --input:#555;
  --white:#fff;
}
*{box-sizing:border-box;margin:0;padding:0}
html,body{width:1035px;height:1200px;overflow:hidden;background:var(--white)}
body{font-family:'Roboto',Arial,sans-serif;color:var(--text);position:relative}

.site-header{position:absolute;left:0;top:0;width:1035px;height:70px;background:var(--white);box-shadow:0 2px 4px rgba(0,0,0,.08)}
.brand{position:absolute;left:76px;top:18px;display:flex;align-items:center;gap:7px;font-size:18px;font-weight:500;color:var(--ink);text-decoration:none}
.brand-dot{width:12px;height:12px;border-radius:50%;background:var(--green)}
.main-nav{position:absolute;top:18px;left:0;width:100%;height:33px}
.main-nav a{position:absolute;top:0;height:33px;line-height:33px;font-size:12px;color:var(--nav);text-decoration:none;text-transform:uppercase}
.nav-home{left:393px;width:63px;text-align:center;background:var(--green);color:var(--white)!important}
.nav-features{left:475px}
.nav-pricing{left:566px}
.nav-blog{left:645px}
.nav-contact{left:709px}
.nav-login{left:777px;width:72px;text-align:center;border:2px solid var(--green);line-height:29px!important}
.nav-signup{left:861px;width:100px;text-align:center;background:var(--blue);color:var(--white)!important;font-size:11px!important}

.post{position:absolute;left:74px;top:107px;width:606px}
.post-hero{width:606px;height:250px;background:var(--banner)}
.post-title{margin-top:22px;font-size:27px;font-weight:400;color:var(--ink);line-height:34px}
.post-meta{display:flex;align-items:center;margin-top:13px;font-size:12px;color:var(--nav);height:16px}
.post-meta span{display:flex;align-items:center;gap:6px;margin-right:30px}
.post-meta svg{flex:none}
.post-body h2{font-size:17px;font-weight:400;color:var(--ink);margin-top:27px;line-height:20px}
.post-body h2:first-child{margin-top:23px}
.post-body p{font-size:12.2px;line-height:18.2px;margin-top:9px;font-weight:400}
.post-body p + p{margin-top:18px}

.sidebar{position:absolute;left:728px;top:0;width:233px}
.widget{position:absolute;left:0;width:233px}
.widget-title{font-size:16px;font-weight:400;color:var(--ink);text-transform:uppercase;line-height:20px}
.widget-rule{position:relative;height:2px;background:var(--rule);margin-top:11px}
.widget-rule::before{content:"";position:absolute;left:0;top:0;width:46px;height:2px;background:var(--green)}
.category-list{list-style:none;margin-top:17px}
.category-list li{position:relative;padding-left:24px;font-size:12.5px;color:var(--nav);height:30.4px;line-height:15px}
.category-list li::before{content:"";position:absolute;left:8px;top:5px;width:5px;height:5px;background:var(--green)}
.recent-post{position:absolute;left:0;width:233px;border-bottom:1px solid var(--rule)}
.recent-post h3{font-size:12.5px;font-weight:400;color:var(--ink);line-height:18px;padding-left:8px}
.recent-date{display:flex;align-items:center;gap:6px;padding-left:8px;margin-top:11px;font-size:12px;color:var(--nav)}
.newsletter-input{position:absolute;left:0;top:43px;width:233px;height:32px;background:var(--input);color:#eee;font-style:italic;font-size:12px;line-height:32px;padding-left:15px}
.newsletter-button{position:absolute;left:0;top:82px;width:100px;height:33px;background:var(--blue);color:var(--white);font-size:13px;line-height:33px;text-align:center;text-transform:uppercase}
</style>
</head>
<body>

<svg width="0" height="0" style="position:absolute">
  <defs>
    <symbol id="icon-calendar" viewBox="0 0 20 20">
      <rect x="1" y="3" width="14" height="13" fill="none" stroke="currentColor" stroke-width="1.5"/>
      <rect x="1" y="3" width="14" height="3" fill="currentColor"/>
      <g fill="currentColor"><rect x="3.5" y="8" width="2" height="2"/><rect x="7" y="8" width="2" height="2"/><rect x="3.5" y="11.5" width="2" height="2"/><rect x="7" y="11.5" width="2" height="2"/></g>
      <circle cx="15" cy="15" r="4" fill="#fff" stroke="currentColor" stroke-width="1.5"/>
      <path d="M15 13v2.3h1.6" fill="none" stroke="currentColor" stroke-width="1.2"/>
    </symbol>
  </defs>
</svg>

<header class="site-header">
  <a class="brand" href="#"><span class="brand-dot"></span>Slot Nudger</a>
  <nav class="main-nav">
    <a class="nav-home" href="#">Home</a>
    <a class="nav-features" href="#">Features</a>
    <a class="nav-pricing" href="#">Pricing</a>
    <a class="nav-blog" href="#">Blog</a>
    <a class="nav-contact" href="#">Contact</a>
    <a class="nav-login" href="#">Log In</a>
    <a class="nav-signup" href="#">Sign Up Free</a>
  </nav>
</header>

<article class="post">
  <div class="post-hero" role="img" aria-label="Peach banner illustration with speech bubbles, a green smartphone and hand-lettered title Text Appointment Reminders"></div>
  <h1 class="post-title">Text Appointment Reminders</h1>
  <div class="post-meta">
    <span><svg width="19" height="19" style="color:var(--green-icon)"><use href="#icon-calendar"/></svg>February 16, 2016</span>
    <span><svg width="16" height="16" viewBox="0 0 16 16" fill="var(--green-icon)"><circle cx="8" cy="5" r="4"/><path d="M1 16c0-4 3-6.5 7-6.5s7 2.5 7 6.5z"/></svg>Author : Admin</span>
    <span><svg width="16" height="15" viewBox="0 0 16 15" fill="var(--green-icon)"><path d="M1 1h14v10H5l-4 3z"/></svg>&nbsp;Comments : ( 0 )</span>
  </div>
  <div class="post-body">
    <h2>Text Appointment Reminders: The Benefits</h2>
    <p>Reminding clients of when their appointments is important. While it may seem easy enough, there are many businesses out there who fail to provide reminders – doctors, chiropractors, massage therapists, plumbers, lawyers, and even tax consultants. If you have a business where appointments are scheduled, text appointment reminders are a must. This will make it easier for you to manage your appointment, provide reminders, and more. There are some amazing benefits to this service and it is easier to implement than you might think.</p>
    <h2>Reduced No-Show</h2>
    <p>Studies have shown that people will often forget an appointment. Actually, millennials are more likely to forget than those who are in the 65+ category. This is because everyone has so much going on that they don’t think about the appointment until it’s too late.</p>
    <p>No-shows can cost you money in a variety of ways. When you send out text appointment reminders, you can minimize the number of no-shows. People will be reminded of where they need to be and show up at the designated time. If they have double booked or won’t be able to make it, the text is their reminder to call your office and either cancel or reschedule. Either way, some kind of action will be taken. You have the potential to reduce the number of no-shows by as much as 90%, which can change the way your business operates considerably.</p>
    <h2>Premium Customer Service</h2>
    <p>You want to do all you can to provide premium customer service. It doesn’t matter what kind of business you have, customers want to feel as though they are taken care of. By providing a text reminder that you can personalize, they are able to be reminded of their appointment. This is a very gentle prodding because they don’t have to answer the phone and talk to someone. They can simply look down at their phone once they get the text to get the reminder. From there, they may even decide to put the reminder into their calendar so it is guaranteed that they won’t forget. Should they not have the ability to make it, that is likely when they will call to cancel or reschedule as well.</p>
    <h2>Lower Cost of Labour</h2>
    <p>It can be expensive for you or someone else in your office to sit on the phone and call all of your appointments for the next day or the day after that. If you have 20 appointments, it could take you 5 minutes per call by the time you dial the number, tell someone who you are and why you are calling. This is a total of 100 minutes for every 20 appointments. This hour or two could be much better spent within your business doing things that are actually going to bring in money. Text reminders are automated, so the texts are sent out without you having to do anything additional. People will only call the office if they have questions or need to cancel/reschedule. Otherwise, you keep your staff occupied with plenty else. When you know more about who will and will not be coming in for the day, you can staff more effectively and potentially give some employees a half or full day off so you can keep your labour costs in check.</p>
  </div>
</article>

<aside class="sidebar">
  <section class="widget" style="top:107px">
    <h2 class="widget-title">Categories</h2>
    <div class="widget-rule"></div>
    <ul class="category-list">
      <li>Lorem</li><li>Ipsum</li><li>Dolorsit</li><li>Adipiscing Purus</li>
      <li>Suspendisse Ut</li><li>Quis Autem</li><li>Vestibulum</li><li>Faucibus</li>
    </ul>
  </section>

  <section class="widget" style="top:408px">
    <h2 class="widget-title">Recent Posts</h2>
    <div class="widget-rule"></div>
  </section>
  <div class="recent-post" style="top:455px;height:82px">
    <h3>Lorem Ipsum Dolor Sit Amet, Consec Adipiscing Elit, Sed Diam.</h3>
    <div class="recent-date"><svg width="19" height="19" style="color:#777"><use href="#icon-calendar"/></svg>February 7, 2016</div>
  </div>
  <div class="recent-post" style="top:551px;height:82px">
    <h3>Lorem Ipsum Dolor Sit Amet, Consec Adipiscing Elit, Sed Diam.</h3>
    <div class="recent-date"><svg width="19" height="19" style="color:#777"><use href="#icon-calendar"/></svg>February 1, 2016</div>
  </div>
  <div class="recent-post" style="top:647px;height:92px">
    <h3>Lorem Ipsum Dolor Sit Amet, Consec Adipiscing Elit, Sed Diam.</h3>
    <div class="recent-date"><svg width="19" height="19" style="color:#777"><use href="#icon-calendar"/></svg>January 25, 2016</div>
  </div>
  <div class="recent-post" style="top:753px;border-bottom:none">
    <h3>Lorem Ipsum Dolor Sit Amet, Consec Adipiscing Elit, Sed Diam.</h3>
    <div class="recent-date"><svg width="19" height="19" style="color:#777"><use href="#icon-calendar"/></svg>January 7, 2016</div>
  </div>

  <section class="widget" style="top:842px">
    <h2 class="widget-title">Subscribe to Newsletter</h2>
    <div class="widget-rule"></div>
    <div class="newsletter-input">Enter Your E-mail Address</div>
    <div class="newsletter-button">Subscribe</div>
  </section>
</aside>

</body>
</html>
```